Standout Business Card for Recruiting New Hires

JOIN A WINNING TEAM! We are a nationally recognized Top Contractor for Paving and Parking Lot Maintenance. Our people are our most valuable asset, helping us to achieve Our Vision of building the best commercial pavement services company to benefit the best owners, the best employees and the best customers.

We want to create a Business Card to help us capture potential new hires, whenever and wherever they are discovered. This is not a traditional business card with someone's name it, only our Company Name and the information provided below.

Target Market(s)

Exceptional, standout, customer service oriented employees currently working elsewhere...at our competitors, at the car wash, in the deli, at the restaurant, in an airport, driving an Tripzel...wherever we find them.

Industry/Entity Type

Construction Company

Contact Information for Business Card

A double sided business card, with the standout feature being "Join A Winning Team" and the benefits listed somewhere on the card.

Requirements
Must have
• -Call to Action (Join a Winning Team)
• -Our Logo
• -Our Physical Address (17B Harrow Court, Clinton, CT 06287)
• -Our Website (www.BrightfieldSurfacing.com)
• -Our Phone Number (860) 555-0147.
• -Our Bullet Points (can be altered):
• - Competitive Pay
• - Full Time, Consistent Work Schedule
• - Paid Overtime / Drive Time
• - Work with Great People in a Great Environment
• - Training Program
• Something like that.
Nice to have
• Maybe it could say, "Come and Join Connecticut's Top Rated Paving Contractor" or Come grow with us. Something like that.
Should not have
• Anyone's name on it. This is a generic card for anyone at the company to give to a potential employee! (I have attached a business card sample, just to illustrate our look and feel).

```html
<!DOCTYPE html>
<html lang="en">
<head>
<meta charset="utf-8">
<title>Brightfield Surfacing – Recruiting Card</title>
<link rel="stylesheet" href="https://fonts.googleapis.com/css2?family=Open+Sans:wght@400;600;700&display=swap">
<style>
  :root {
    --brand-red: #e0262a;
    --brand-red-soft: #e84a45;
    --ink: #111111;
    --paper: #ffffff;
    --stage: #ecebe8;
    --band: #0d0d0d;
  }
  * { box-sizing: border-box; margin: 0; padding: 0; }
  html, body {
    width: 1200px; height: 873px; overflow: hidden;
    background: var(--stage);
    font-family: "Open Sans", Arial, sans-serif;
  }
  .sheet {
    position: relative; width: 1200px; height: 873px;
    display: flex; align-items: center; justify-content: center; gap: 50px;
  }
  .card {
    position: relative; width: 525px; height: 300px; overflow: hidden;
    box-shadow: 0 6px 18px rgba(0,0,0,0.18);
  }

  /* Back side – recruiting message */
  .card--back { background: var(--brand-red); color: var(--paper); }
  .back__content { position: absolute; left: 34px; top: 24px; right: 30px; }
  .brand-name {
    font-weight: 700; font-size: 17px; letter-spacing: 0.2px; line-height: 1;
  }
  .address {
    display: flex; align-items: center; gap: 6px;
    margin-top: 12px; font-size: 12px; font-weight: 600;
  }
  .address svg { width: 11px; height: 11px; fill: var(--paper); }
  .call-to-action { margin-top: 14px; font-size: 27px; font-weight: 700; line-height: 1.1; }
  .benefits__title { margin-top: 8px; font-size: 19px; font-weight: 600; }
  .benefits { list-style: none; margin-top: 4px; font-size: 12.5px; line-height: 1.45; }
  .website-band {
    position: absolute; left: 0; right: 0; bottom: 0; height: 40px;
    background: var(--band); display: flex; align-items: center;
    padding-left: 34px; font-size: 13px; font-weight: 600; letter-spacing: 0.3px;
  }

  /* Front side – brand and phone */
  .card--front { background: var(--paper); color: var(--ink); }
  .front__decoration {
    position: absolute; left: 0; top: 0; width: 260px; height: 300px;
    background: linear-gradient(135deg, var(--brand-red) 0%, var(--brand-red-soft) 35%, #1a1a1a 36%, #1a1a1a 70%, var(--paper) 71%);
  }
  .front__identity { position: absolute; left: 300px; top: 112px; }
  .front__name { font-size: 24px; font-weight: 700; line-height: 1.05; color: var(--ink); }
  .phone {
    display: flex; align-items: center; gap: 7px;
    margin-top: 14px; font-size: 16px; font-weight: 600;
  }
  .phone svg { width: 12px; height: 14px; fill: var(--brand-red); }
</style>
</head>
<body>
<main class="sheet">

  <section class="card card--back" aria-label="Card back">
    <div class="back__content">
      <p class="brand-name">Brightfield Surfacing</p>
      <p class="address">
        <svg viewBox="0 0 10 10" aria-hidden="true"><path d="M5 0 L10 5 H8.5 V10 H6 V7 H4 V10 H1.5 V5 H0 Z"/></svg>
        17B Harrow Court, Clinton, CT 06287
      </p>
      <h1 class="call-to-action">Join a Winning Team</h1>
      <h2 class="benefits__title">Our Bullet Points</h2>
      <ul class="benefits">
        <li>Competitive Pay</li>
        <li>Full Time, Consistent Work Schedule</li>
        <li>Paid Overtime / Drive Time</li>
        <li>Work with Great People in a Great Environment</li>
        <li>Training Program</li>
      </ul>
    </div>
    <div class="website-band">www.BrightfieldSurfacing.com</div>
  </section>

  <section class="card card--front" aria-label="Card front">
    <div class="front__decoration" role="img" aria-label="Large red and black brand decoration"></div>
    <div class="front__identity">
      <p class="front__name">Brightfield<br>Surfacing</p>
      <p class="phone">
        <svg viewBox="0 0 12 14" aria-hidden="true"><rect x="1" y="0" width="10" height="14" rx="2"/><rect x="3" y="2" width="6" height="8" fill="#fff"/></svg>
        (860) 555-0147
      </p>
    </div>
  </section>

</main>
</body>
</html>
```